Sanora-Velantis Flyer Patient Day

We need a flyer for an event (format A5, double-sided, portrait format). This event is aimed at lymphology patients. The aim of this case is to inform patients about the progress of treatment, to show trends and to get in touch with them. The structure of the Flyer must be follows: - Page 1: with the title and date and logo of Sanora-Velantis - Page 2: with info text and details of the event The text templates are attached below: (180216_VA_Briefing_Workshopflyer_Betroffenentag_Sanora-Velantis.docx) The logos for the partners are also attached below. The following design inputs: 1) Please visit the following website: www.sanora-velantis.ch and use the logo of Sanora-Velantis 2) The visual language should be appropriate for the theme of networking (No Go people, preferably using graphical elements. ) Please use elements of the lymphology pathways, 3) For texts please use the following font: Roboto-Light For running text please use the following font: PT-Serif-Italic, sans-serif 4) The texts must be reader-friendly Please note that this flyer is not for Brevido, but for Sanora-Velantis.

```html
<!DOCTYPE html>
<html lang="de">
<head>
<meta charset="utf-8">
<title>Sanora-Velantis – Betroffenen- und Angehörigentag</title>
<link href="https://fonts.googleapis.com/css2?family=Roboto:wght@300;400;500;700&family=Ubuntu:wght@400;500;700&display=swap" rel="stylesheet">
<style>
  :root {
    --green-dark: #16a04a;
    --green-mid: #8cc63f;
    --green-light: #c6e2a0;
    --green-pale: #f3f7ea;
    --navy: #1b3f8b;
    --navy-deep: #15224f;
    --blood-dark: #3a0608;
    --blood: #a8141a;
    --ink: #2a2a2a;
    --bg: #e9e9e6;
  }
  * { margin: 0; padding: 0; box-sizing: border-box; }
  html, body { width: 1200px; height: 960px; overflow: hidden; }
  body {
    background: var(--bg);
    font-family: "Roboto", sans-serif;
    color: var(--ink);
    position: relative;
  }
  .page {
    position: absolute;
    top: 66px;
    width: 544px;
    height: 771px;
    overflow: hidden;
    box-shadow: 0 14px 24px rgba(0,0,0,.25);
  }
  .page--front { left: 39px; background: #fff; }
  .page--back { left: 622px; background: var(--green-pale); }
  .page svg.backdrop { position: absolute; inset: 0; }

  /* front */
  .brand-mark {
    position: absolute; left: 400px; top: 404px;
    display: flex; align-items: center; gap: 7px;
    font-family: "Ubuntu", sans-serif; font-weight: 500; font-size: 15px; color: #fff;
  }
  .brand-mark .square { width: 13px; height: 13px; background: #fff; flex: none; }
  .event-title {
    position: absolute; right: 26px; top: 502px;
    text-align: right; font-weight: 300; font-size: 35px; line-height: 41px; color: var(--navy);
  }
  .event-date {
    position: absolute; right: 30px; top: 646px;
    font-weight: 700; font-size: 30px; line-height: 36px; color: var(--navy);
  }
  .front-footer {
    position: absolute; left: 0; right: 0; top: 693px; height: 78px; background: #fff;
  }
  .partner-a {
    position: absolute; left: 190px; top: 40px;
    font-size: 7px; line-height: 9px; font-weight: 500; color: var(--ink);
  }
  .partner-b {
    position: absolute; left: 322px; top: 18px;
    display: flex; align-items: center; gap: 8px;
  }
  .partner-b .circle { width: 28px; height: 28px; border-radius: 50%; background: var(--green-dark); flex: none; }
  .partner-b p { font-size: 8px; line-height: 10px; color: var(--ink); }

  /* back */
  .intro {
    position: absolute; left: 34px; top: 21px; width: 486px;
    font-family: "Ubuntu", sans-serif; font-weight: 700; font-size: 15.5px; line-height: 17px; color: var(--green-dark);
  }
  .facts {
    position: absolute; left: 82px; top: 127px; width: 372px;
    border-collapse: separate; border-spacing: 0 4px; font-size: 13px;
  }
  .facts th { width: 86px; text-align: left; padding: 2px 0 2px 12px; vertical-align: top; font-weight: 700; color: var(--navy-deep); }
  .facts td { padding: 2px 8px; color: var(--navy); line-height: 17px; }
  .facts tr.strong th { background: #6cc04a; }
  .facts tr.strong td { background: var(--green-mid); }
  .facts tr.soft th { background: #a9d67e; }
  .facts tr.soft td { background: var(--green-light); }
  .programme { position: absolute; left: 34px; top: 302px; }
  .programme h2 { font-family: "Ubuntu", sans-serif; font-weight: 500; font-size: 19px; color: var(--navy); margin-bottom: 6px; }
  .programme ul { list-style: none; font-size: 13.5px; color: var(--ink); }
  .programme > ul > li { padding-left: 16px; position: relative; line-height: 22.5px; }
  .programme > ul > li::before { content: "✓"; position: absolute; left: 0; color: var(--navy); font-size: 11px; }
  .programme ul ul { margin: 2px 0 2px 12px; }
  .programme ul ul li { padding-left: 16px; position: relative; line-height: 17.5px; }
  .programme ul ul li::before {
    content: ""; position: absolute; left: 0; top: 6px;
    width: 7px; height: 7px; border-radius: 50%; background: var(--green-mid);
  }
  .back-brand {
    position: absolute; left: 352px; top: 438px;
    display: flex; align-items: center; gap: 8px;
    font-family: "Ubuntu", sans-serif; font-weight: 500; font-size: 19px; color: var(--navy-deep);
  }
  .back-brand .square { width: 16px; height: 16px; background: var(--green-mid); }
  .admission { position: absolute; left: 34px; top: 604px; font-size: 13.5px; color: var(--ink); }
  .admission .row { display: flex; margin-bottom: 8px; }
  .admission .label { font-family: "Ubuntu", sans-serif; font-weight: 700; color: var(--navy); margin-right: 8px; }
  .admission .eintritt .label { width: 56px; margin-right: 14px; }
  .admission .eintritt p { line-height: 17px; }
  .sponsor-band {
    position: absolute; left: 0; right: 0; top: 692px; height: 79px; background: var(--green-mid);
    display: flex; align-items: center; justify-content: space-around; padding: 0 30px;
  }
  .sponsor { font-family: "Roboto", sans-serif; font-weight: 500; font-size: 17px; color: var(--navy-deep); }
</style>
</head>
<body>

<section class="page page--front" aria-label="Flyer Vorderseite">
  <svg class="backdrop" viewBox="0 0 544 771" width="544" height="771">
    <defs>
      <radialGradient id="bloodGlow" cx="55%" cy="40%" r="70%">
        <stop offset="0" stop-color="#a8141a"/>
        <stop offset="1" stop-color="#3a0608"/>
      </radialGradient>
    </defs>
    <path class="frame-strip" d="M0 0 H8 V118 Q90 250 190 400 Q70 300 0 400 Z" fill="var(--green-dark)"/>
    <path class="green-field" d="M544 290 L544 486 Q360 494 150 490 L210 395 Q330 320 544 290 Z" fill="var(--green-dark)"/>
    <path role="img" aria-label="Illustration: Blutgefäss mit roten und weissen Blutkörperchen"
          d="M8 0 H544 V298 Q330 325 205 410 Q90 300 8 118 Z" fill="url(#bloodGlow)"/>
    <path class="sweep" d="M57 771 Q110 430 544 298 L544 320 Q180 425 105 771 Z" fill="var(--green-light)"/>
    <rect class="date-band" x="160" y="640" width="384" height="51" fill="var(--green-light)"/>
    <rect x="160" y="636" width="384" height="2" fill="#dcecc6"/>
  </svg>
  <div class="brand-mark"><span class="square"></span>Sanora-Velantis</div>
  <h1 class="event-title">Betroffenen- und<br>Angehörigentag Lip-<br>und Lymphödem</h1>
  <p class="event-date">16. Jun 2018</p>
  <footer class="front-footer">
    <div class="partner-a">Lymphödem Netzwerk Schweiz</div>
    <div class="partner-b">
      <span class="circle"></span>
      <p>lipödem forum schweiz<br>forum lipoedème suisse<br>forum lipedema svizzera<br>swiss lipedema forum</p>
    </div>
  </footer>
</section>

<section class="page page--back" aria-label="Flyer Rückseite">
  <svg class="backdrop" viewBox="0 0 544 771" width="544" height="771">
    <path d="M0 75 Q260 140 544 70" fill="none" stroke="var(--green-mid)" stroke-width="1.5"/>
    <path d="M0 95 Q300 120 544 55" fill="none" stroke="var(--navy)" stroke-width="1.2"/>
    <path d="M6 226 Q120 310 300 306 Q440 300 544 300 L544 318 Q430 318 300 322 Q120 328 6 226 Z" fill="var(--green-mid)"/>
    <path d="M0 585 Q260 520 544 620 Q260 545 0 600 Z" fill="var(--green-mid)"/>
  </svg>
  <p class="intro">Die Stiftung Sanora-Velantis organisiert mit den beiden Betroffenenorganisationen Lipödem Forum Schweiz und Lymphödem Netzwerk Schweiz die folgende Tagung:</p>
  <table class="facts">
    <tr class="strong"><th>Datum</th><td>16. Juni 2018</td></tr>
    <tr class="soft"><th>Zeit</th><td>ab 9h00 Eintreffen der Besucher<br>(Industrieausstellung geöffnet)<br>ab 10h00 Start des Tagungsprogramms</td></tr>
    <tr class="strong"><th>Ort</th><td>TBD, Aarau</td></tr>
    <tr class="soft"><th>Zielgruppe</th><td>Betroffene und Angehörige</td></tr>
  </table>
  <div class="programme">
    <h2>Programme</h2>
    <ul>
      <li>Industrieausstellung</li>
      <li>Darstellung Lip- und Lymphödem</li>
      <li>Vorstellung der Organisationen
        <ul>
          <li>Stiftung Sanora-Velantis</li>
          <li>Lipödem Forum Schweiz</li>
          <li>Lymphödem Netzwerk Schweiz</li>
        </ul>
      </li>
      <li>Ausgewogene Ernährung</li>
      <li>Mode für Betroffene</li>
      <li>Sport als Bestandteil der Therapie</li>
    </ul>
  </div>
  <div class="back-brand"><span class="square"></span>Sanora-Velantis</div>
  <div class="admission">
    <div class="row eintritt"><span class="label">Eintritt:</span><p>Teilnahmegebühren inkl. Mittagessen CHF 50.- pro Person,<br>jede weitere Person CHF 15.-</p></div>
    <div class="row"><span class="label">Anmeldungen und Fragen via E-mail :</span><span>info@sanora-velantis.ch</span></div>
    <div class="row"><span class="label">Anmeldefrist:</span><span>20 Mai 2018</span></div>
  </div>
  <footer class="sponsor-band">
    <span class="sponsor">VALMERA</span>
    <span class="sponsor">Brevido</span>
    <span class="sponsor">KORIN medical</span>
    <span class="sponsor">TELVO</span>
  </footer>
</section>

</body>
</html>
```